Sports Nutrition line needs new label look/feel

We need a new label design for "Telmo",our Sports Nutrition line of vitamins, nutraceuticals, protein powders, and performance endurance products. We would like to see two separate designs, one blue and one red, as these are the two colors we are torn between. The labels should have the look/feel of a sports or fitness label, bold coloring, lettering, and even some use of holographic foiling.
Brands we would be similar to those found on pulsevaultshop.com and stridecraftnow.com. Brands we like in particular are QRT and Velmot.

Target Market(s)

Fitness enthusiasts,athletes, health nuts..

Industry/Entity Type

Nutrition

Font styles to use
Sans Serif
Decorative
Script

Colors
ec1f27
0692cd
0355a3
3276b5
f04a50

Requirements
Must have
• -Fitness look/feel
• -bold colors (preferably red and blue)
• -use of icons (eye health, brain, health, etc.)
• -"Fit" in "TelMO" must stand out
• -use tagline "Building Healthy Bodies"
Nice to have
• -holographic foiling elements
• -try to incorporate a molecular element (like those shown in the example labels)
Should not have
• -Light, calming colors
• -difficult to read fonts

```html
<!DOCTYPE html>
<html lang="en">
<head>
<meta charset="utf-8">
<title>TelMO – Loaded Nutrition Label</title>
<link rel="stylesheet" href="https://fonts.googleapis.com/css2?family=Hind:wght@500;600&family=Montserrat:wght@600;800&display=swap">
<style>
  :root{
    --page:#ffffff;
    --label-dark:#1c1c1e;
    --stripe-light:#3a3a3d;
    --stripe-dark:#151517;
    --panel:#2a2a2c;
    --red:#ec1f27;
    --red-soft:#f04a50;
    --red-deep:#7a0d12;
    --white:#ffffff;
  }
  *{margin:0;padding:0;box-sizing:border-box}
  html,body{width:1200px;height:1200px;overflow:hidden;background:var(--page)}
  .label{
    position:absolute;left:100px;top:156px;width:1000px;height:887px;overflow:hidden;
    background:repeating-linear-gradient(180deg,var(--stripe-light) 0 8px,var(--label-dark) 8px 26px,var(--stripe-dark) 26px 40px);
  }
  .side-panels{position:absolute;inset:0}
  .top-rule{position:absolute;left:0;top:0;width:100%;height:28px;
    background:linear-gradient(180deg,var(--label-dark) 0 6px,var(--red) 6px 12px,var(--red-deep) 12px 22px,var(--label-dark) 22px)}
  .logo-band{position:absolute;left:130px;top:249px;width:740px;height:133px;
    background:linear-gradient(90deg,transparent,var(--red-deep) 12%,var(--red) 35%,var(--red-soft) 50%,var(--red) 65%,var(--red-deep) 88%,transparent)}
  .brand{position:absolute;left:0;width:100%;top:258px;display:flex;justify-content:center;align-items:center;gap:16px;
    font-family:"Hind",sans-serif;font-weight:600;font-size:82px;color:var(--white);line-height:1}
  .brand-mark{width:44px;height:44px;border-radius:50%;background:var(--white)}
  .tagline{position:absolute;left:0;width:100%;top:340px;text-align:center;
    font-family:"Hind",sans-serif;font-weight:600;font-size:30px;color:var(--white)}
  .nutrition-band{position:absolute;left:150px;top:398px;width:700px;height:37px;
    background:linear-gradient(90deg,transparent,var(--red) 15%,var(--red-soft) 50%,var(--red) 85%,transparent);
    display:flex;justify-content:center;align-items:center;
    font-family:"Hind",sans-serif;font-weight:500;font-size:34px;letter-spacing:1px;color:var(--white)}
  .strength-pill{position:absolute;left:301px;top:471px;width:385px;height:38px;border-radius:19px;
    border:2px solid var(--red);background:linear-gradient(90deg,var(--red-deep),#3b0a0c 50%,var(--red-deep));
    display:flex;justify-content:center;align-items:center;
    font-family:"Montserrat",sans-serif;font-weight:800;font-size:31px;letter-spacing:-1px;color:var(--white)}
  .flavor{position:absolute;left:193px;top:582px;font-family:"Montserrat",sans-serif;color:var(--white)}
  .flavor-name{font-weight:800;font-size:19px;letter-spacing:-.5px}
  .flavor-note{font-weight:600;font-size:12px;margin-top:2px}
  .net-weight{position:absolute;right:204px;top:584px;text-align:right;font-family:"Montserrat",sans-serif;color:var(--white)}
  .net-weight-amount{font-weight:800;font-size:18px}
  .net-weight-type{font-weight:800;font-size:12px;margin-top:3px}
  .bottom-rule{position:absolute;left:0;top:812px;width:100%;height:75px;
    background:linear-gradient(180deg,var(--red-deep) 0 4px,var(--label-dark) 4px 10px,var(--red) 10px 18px,var(--label-dark) 18px)}
</style>
</head>
<body>
<div class="label">
  <svg class="side-panels" width="1000" height="887" viewBox="0 0 1000 887" aria-hidden="true">
    <polygon points="0,32 320,32 4,698 0,698" fill="#2a2a2c" opacity=".9"/>
    <polygon points="680,32 1000,32 1000,698" fill="#2a2a2c" opacity=".9"/>
    <line x1="320" y1="32" x2="4" y2="698" stroke="#ec1f27" stroke-width="4"/>
    <line x1="680" y1="32" x2="1000" y2="698" stroke="#ec1f27" stroke-width="4"/>
    <line x1="320" y1="32" x2="680" y2="32" stroke="#555" stroke-width="2"/>
  </svg>
  <div class="top-rule"></div>
  <div class="logo-band"></div>
  <div class="brand"><span class="brand-mark"></span><span class="brand-name">TelMO</span></div>
  <div class="tagline">Building Healthy Bodies</div>
  <div class="nutrition-band">LOADED NUTRITION</div>
  <div class="strength-pill">EXTRA STRENGTH</div>
  <div class="flavor">
    <div class="flavor-name">FRUIT PUNCH</div>
    <div class="flavor-note">Natural Flavor</div>
  </div>
  <div class="net-weight">
    <div class="net-weight-amount">550g/ 19.4 Oz 35 Servings</div>
    <div class="net-weight-type">DIETARY SUPPLEMENT</div>
  </div>
  <div class="bottom-rule"></div>
</div>
</body>
</html>
```